Lodging Venture Advisors

I am an independent operator engaged on short/medium term consultancy briefs within the Hotel/Resort sector in the Pacific Area and have a representation in Fiji.

A broad based services is offered and includes:

Development Advisory
Property Management
Sales & Marketing
Holiday Ownership/Timeshare
Resorts/Apartments/Motels/Flashpackers/B&B
Financial & Legal Referrals

Industry/Entity Type

Hotel

Contact Information for Business Card

Business name - LODGING VENTURE ADVISORS
My name - Grant Whitlock
Address: PO Box 382 Coral Heights 4219 Qld
Phone: Australia: +61 7 55904283 Mobile: 0418952064 (Viber)
Fiji: +679 8527319
Email: grantmwhitlock@netmailbox.example

```html
<!DOCTYPE html>
<html lang="en">
<head>
<meta charset="utf-8">
<title>Lodging Venture Advisors – Business Card</title>
<link rel="stylesheet" href="https://fonts.googleapis.com/css2?family=Oswald:wght@300&family=Source+Sans+3:wght@400&display=swap">
<style>
  :root {
    --backdrop: #ece7df;
    --card-white: #ffffff;
    --card-taupe: #b2aa9c;
    --ink-grey: #5f5f5f;
    --ink-taupe: #8a8276;
    --rule-grey: #6d6d6d;
    --accent-gold: #e2aa2a;
    --ink-light: #ffffff;
    --card-shadow: rgba(60, 45, 30, 0.28);
  }
  html, body {
    margin: 0;
    padding: 0;
    overflow: hidden;
  }
  body {
    width: 1200px;
    height: 696px;
    background: var(--backdrop);
    position: relative;
    font-family: "Source Sans 3", Arial, sans-serif;
  }
  .card {
    position: absolute;
    width: 494px;
    height: 305px;
    box-shadow: 6px 10px 18px var(--card-shadow);
    box-sizing: border-box;
  }

  /* Front */
  .card-front {
    left: 80px;
    top: 70px;
    background: var(--card-white);
  }
  .brand {
    position: absolute;
    left: 0;
    top: 0;
    width: 246px;
    height: 305px;
    display: flex;
    flex-direction: column;
    align-items: center;
    justify-content: center;
    gap: 10px;
  }
  .brand-mark {
    width: 50px;
    height: 50px;
    background: var(--accent-gold);
  }
  .brand-name {
    font-family: "Oswald", "Arial Narrow", sans-serif;
    font-weight: 300;
    font-size: 16px;
    letter-spacing: 0.2px;
    color: var(--ink-taupe);
    white-space: nowrap;
  }
  .divider {
    position: absolute;
    left: 246px;
    top: 37px;
    width: 1.5px;
    height: 238px;
    background: var(--rule-grey);
  }
  .contact {
    position: absolute;
    left: 280px;
    top: 77px;
    color: var(--ink-grey);
  }
  .contact-name {
    margin: 0 0 22px;
    font-size: 18px;
    font-weight: 400;
  }
  .contact-lines {
    margin: 0;
    font-size: 11.5px;
    line-height: 15.6px;
    font-style: normal;
    white-space: nowrap;
  }

  /* Back */
  .card-back {
    left: 627px;
    top: 317px;
    background: var(--card-taupe);
    color: var(--ink-light);
    text-align: center;
  }
  .services-intro {
    margin: 46px 0 22px;
    font-size: 17px;
  }
  .services-list {
    list-style: none;
    margin: 0;
    padding: 0;
    font-size: 17px;
    line-height: 22.3px;
  }
  .back-brand {
    position: absolute;
    right: 10px;
    bottom: 10px;
    display: flex;
    flex-direction: column;
    align-items: flex-end;
    gap: 6px;
  }
  .back-brand .brand-mark {
    width: 36px;
    height: 36px;
    margin-right: 18px;
  }
  .back-brand .brand-name {
    font-size: 11px;
    color: var(--ink-taupe);
  }
</style>
</head>
<body>
  <section class="card card-front" aria-label="Card front">
    <div class="brand">
      <div class="brand-mark"></div>
      <div class="brand-name">LODGING VENTURE ADVISORS</div>
    </div>
    <div class="divider"></div>
    <div class="contact">
      <h1 class="contact-name">Grant Whitlock</h1>
      <address class="contact-lines">
        PO Box 382 Coral Heights 4219<br>
        Qld Phone: Australia: +61 7 55904283<br>
        Mobile: 0418952064 (Viber)<br>
        Fiji: +679 8527319<br>
        grantmwhitlock@netmailbox.example
      </address>
    </div>
  </section>

  <section class="card card-back" aria-label="Card back">
    <p class="services-intro">A broad based service is offered and includes:</p>
    <ul class="services-list">
      <li>Development Advisory</li>
      <li>Property Management</li>
      <li>Sales &amp; Marketing</li>
      <li>Holiday Ownership / Timeshare</li>
      <li>Resorts / Apartments / Motels / Flashpackers / B&amp;B</li>
      <li>Financial &amp; Legal Referrals</li>
    </ul>
    <div class="back-brand">
      <div class="brand-mark"></div>
      <div class="brand-name">LODGING VENTURE ADVISORS</div>
    </div>
  </section>
</body>
</html>
```